Card and board game developer website, small e-commerce site

We are designing a website for Spinning Otter Gadget Works. I need a homepage and a typical inside page designed.
The website navigation will be:
Home (where we'll introduce the games and the website)
Our Games (drops open into the two games)
Griffins of Morvandale
Quintessa
Order Now
About Us
Contact
The header of the website will include the logo, the navigation and a link to a facebook page. The header will also include a cart icon and a link to My Account.
Then on the homepage I suggest we include a row for each game:
Griffins of Morvandale
This row will include a photo (or maybe a series of photos that animate into each other) and quick info about the game plus two buttons: Info and Photos (which will go to the detail page with the photo gallery), and Order Now (which will take you to the product for ordering).
Quintessa
Your footer will contain a copyright note, plus links to:
Terms and conditions
Shipping and returns
FAQ
Contact
Account login
NOTE: the logo is the orange mokey. I've uploaded a brief with more information. The current website that we are redesigning is here https://www.spinningottergadget.example/
Please send me any questions that you have.
People interested in fun card and board games at home.
2 page

```html
<!DOCTYPE html>
<html lang="en">
<head>
<meta charset="utf-8">
<title>Spinning Otter Gadget Works — Home</title>
<link rel="stylesheet" href="https://fonts.googleapis.com/css2?family=DM+Serif+Display&family=Inter:wght@400;500;600&display=swap">
<style>
  :root {
    --backdrop: #f6f5f3;
    --page: #ffffff;
    --hero-bg: #fbfaf8;
    --ink: #111111;
    --muted: #555555;
    --orange: #ec8a2e;
    --orange-soft: #f3b47a;
    --line: #ececec;
    --button-dark: #0d0d0d;
  }
  * { box-sizing: border-box; margin: 0; padding: 0; }
  html, body { width: 1200px; height: 902px; overflow: hidden; }
  body {
    background: var(--backdrop);
    font-family: "Inter", Arial, sans-serif;
    color: var(--ink);
    position: relative;
  }
  .site {
    position: absolute; left: 119px; top: 68px; width: 962px; height: 761px;
    background: var(--hero-bg);
    border: 1px solid var(--line);
    box-shadow: 0 10px 40px rgba(0,0,0,0.05);
    overflow: hidden;
  }
  .site-header {
    position: absolute; left: 0; top: 0; width: 100%; height: 65px;
    background: var(--page);
    border-bottom: 1px solid var(--line);
  }
  .brand {
    position: absolute; left: 145px; top: 20px;
    display: flex; align-items: center; gap: 6px;
    font-size: 10px; font-weight: 600; color: var(--orange); line-height: 1.15;
    width: 110px;
  }
  .brand-dot { width: 14px; height: 14px; border-radius: 50%; background: var(--orange); flex: none; }
  .nav-link {
    position: absolute; top: 25px; font-size: 12.5px; color: var(--ink); text-decoration: none;
  }
  .nav-order {
    position: absolute; left: 461px; top: 16px; width: 126px; height: 35px;
    border-radius: 18px; background: var(--button-dark); color: var(--orange);
    font-size: 13px; font-weight: 500; display: flex; align-items: center; justify-content: center;
    box-shadow: 0 3px 6px rgba(0,0,0,0.25);
    text-decoration: none;
  }
  .cart-button {
    position: absolute; left: 878px; top: 21px; width: 26px; height: 26px;
    border: 1px solid #444; border-radius: 50%;
    display: flex; align-items: center; justify-content: center;
  }
  .hero-title {
    position: absolute; left: 145px; top: 142px; width: 470px;
    font-family: "DM Serif Display", Georgia, serif; font-weight: 400;
    font-size: 33px; line-height: 44px;
  }
  .hero-lead { position: absolute; left: 145px; top: 244px; font-size: 12.2px; font-weight: 500; }
  .hero-text { position: absolute; left: 145px; top: 275px; font-size: 7.6px; line-height: 10px; }
  .btn {
    position: absolute; height: 22px; border-radius: 11px;
    font-size: 9.5px; display: flex; align-items: center; justify-content: center; gap: 5px;
  }
  .btn-primary { background: var(--orange); color: #fff; box-shadow: 0 2px 4px rgba(236,138,46,0.35); }
  .btn-outline { background: #fff; border: 1px solid var(--orange-soft); color: #555; box-shadow: 0 2px 4px rgba(236,138,46,0.15); }
  .btn-accent { background: #fff; border: 1px solid var(--orange); color: var(--orange); font-weight: 500; }
  .hero-box {
    position: absolute; left: 642px; top: 120px; width: 170px; height: 254px;
    background: linear-gradient(180deg, #e6e6e6 0%, #e9e6e2 55%, #e9ac6c 100%);
    box-shadow: -30px 2px 18px -14px rgba(0,0,0,0.35);
  }
  .section-title {
    position: absolute; left: 145px; top: 434px;
    font-family: "DM Serif Display", Georgia, serif; font-weight: 400; font-size: 22px;
  }
  .product-card {
    position: absolute; top: 480px; width: 237px; height: 237px;
    background: var(--page); border: 1px solid var(--line);
  }
  .product-photo { position: absolute; left: 18px; top: 16px; width: 166px; height: 141px; border-radius: 5px; }
  .product-thumb { position: absolute; left: 190px; width: 30px; height: 30px; }
  .fav {
    position: absolute; left: 167px; top: 21px; width: 14px; height: 14px; border-radius: 50%;
    border: 1px solid var(--orange-soft); background: rgba(255,255,255,0.6);
    display: flex; align-items: center; justify-content: center;
  }
  .product-name {
    position: absolute; left: 43px; top: 165px;
    font-family: "DM Serif Display", Georgia, serif; font-size: 12px;
  }
  .product-price { position: absolute; left: 166px; top: 168px; font-size: 5px; color: #777; }
  .product-desc { position: absolute; left: 43px; top: 183px; width: 100px; font-size: 3.6px; line-height: 4.6px; color: #444; }
</style>
</head>
<body>
  <div class="site">
    <header class="site-header">
      <div class="brand"><span class="brand-dot"></span>Spinning Otter Gadget Works</div>
      <a class="nav-link" style="left:317px" href="#">Home</a>
      <a class="nav-link" style="left:373px" href="#">Our Games</a>
      <a class="nav-order" href="#">Order Now</a>
      <a class="nav-link" style="left:609px" href="#">About</a>
      <a class="nav-link" style="left:667px" href="#">Contact</a>
      <div class="cart-button" aria-label="Cart">
        <svg width="13" height="12" viewBox="0 0 13 12" fill="none" stroke="#222" stroke-width="1">
          <path d="M0.5 1h2l1.5 6.5h6.5l1.5-4.5H3.2"/><circle cx="5" cy="10" r="0.9"/><circle cx="9.5" cy="10" r="0.9"/>
        </svg>
      </div>
    </header>

    <h1 class="hero-title">Welcome to Spinning Otter Gadget Works</h1>
    <p class="hero-lead">Order Now and Embark on a Journey of Fun and Strategy!</p>
    <p class="hero-text">Immerse Yourself in the World of Griffins with "Griffins of Morvandale"<br>Master the Elements in the Fast-Paced Card Game "Quintessa"</p>
    <a class="btn btn-primary" style="left:146px;top:325px;width:85px">Explore Games</a>
    <a class="btn btn-outline" style="left:247px;top:325px;width:86px">View Artist</a>

    <div class="hero-box" role="img" aria-label="Game box with the studio mascot artwork"></div>

    <h2 class="section-title">Featured</h2>

    <article class="product-card" style="left:145px">
      <div class="product-photo" role="img" aria-label="Photo of the Griffins of Morvandale board game box" style="background:linear-gradient(135deg,#c9d3de 0%,#5b7690 45%,#7a2a2e 75%,#b9bccb 100%)"></div>
      <div class="fav"><svg width="7" height="6" viewBox="0 0 7 6" fill="none" stroke="#ec8a2e" stroke-width="0.7"><path d="M3.5 5.5L1 3a1.3 1.3 0 012.5-1.8A1.3 1.3 0 016 3z"/></svg></div>
      <div class="product-thumb" style="top:21px;background:linear-gradient(#3d6a3a,#7a5a30)" role="img" aria-label="Board game cover"></div>
      <div class="product-thumb" style="top:55px;background:linear-gradient(#9fb79a,#d8d2c4)" role="img" aria-label="Game board in play"></div>
      <div class="product-thumb" style="top:88px;background:linear-gradient(#bfbfbf,#6a4a3a)" role="img" aria-label="Game pieces and cards"></div>
      <div class="product-thumb" style="top:122px;background:linear-gradient(#1e2a18,#57703a)" role="img" aria-label="Card artwork"></div>
      <h3 class="product-name" style="left:43px">Griffins of Morvandale</h3>
      <span class="product-price" style="left:180px">$54.95</span>
      <p class="product-desc">Meet Griffins of Morvandale, the first board game where every player is a griffin</p>
      <a class="btn btn-outline" style="left:18px;top:205px;width:86px">Learn More</a>
      <a class="btn btn-accent" style="left:117px;top:205px;width:102px">
        <svg width="11" height="10" viewBox="0 0 13 12" fill="none" stroke="#ec8a2e" stroke-width="1"><path d="M0.5 1h2l1.5 6.5h6.5l1.5-4.5H3.2"/><circle cx="5" cy="10" r="0.9"/><circle cx="9.5" cy="10" r="0.9"/></svg>Add to Cart</a>
    </article>

    <article class="product-card" style="left:420px">
      <div class="product-photo" role="img" aria-label="Photo of the Quintessa card deck box" style="background:linear-gradient(135deg,#e4e4e4 0%,#3a2a22 35%,#8a3a1a 60%,#eeeeee 100%)"></div>
      <div class="fav"><svg width="7" height="6" viewBox="0 0 7 6" fill="none" stroke="#ec8a2e" stroke-width="0.7"><path d="M3.5 5.5L1 3a1.3 1.3 0 012.5-1.8A1.3 1.3 0 016 3z"/></svg></div>
      <div class="product-thumb" style="top:21px;background:linear-gradient(#6a2a20,#3a6a4a)" role="img" aria-label="Card artwork detail"></div>
      <div class="product-thumb" style="top:55px;background:linear-gradient(#d8cbb8,#5a4030)" role="img" aria-label="Cards laid out"></div>
      <div class="product-thumb" style="top:88px;background:linear-gradient(#e8e2d8,#c9a070)" role="img" aria-label="Cards in hand"></div>
      <div class="product-thumb" style="top:122px;background:linear-gradient(#5a2a1a,#e8e8e8)" role="img" aria-label="Deck box"></div>
      <h3 class="product-name" style="left:43px">Quintessa</h3>
      <span class="product-price" style="left:166px">$14.95</span>
      <p class="product-desc">Welcome to Quintessa, a fast-paced card game of strategy and chance.</p>
      <a class="btn btn-outline" style="left:18px;top:205px;width:86px">Learn More</a>
      <a class="btn btn-accent" style="left:117px;top:205px;width:102px">
        <svg width="11" height="10" viewBox="0 0 13 12" fill="none" stroke="#ec8a2e" stroke-width="1"><path d="M0.5 1h2l1.5 6.5h6.5l1.5-4.5H3.2"/><circle cx="5" cy="10" r="0.9"/><circle cx="9.5" cy="10" r="0.9"/></svg>Add to Cart</a>
    </article>
  </div>
</body>
</html>
```